Either a trifold or double sided flyer/brochure

A flyer to help spark interest in a historic preservation project in Peterborough, NH--looking for something that captures the early 19th century rural village and mill times--American Primitive, Shaker, Cross Stitch Sampler...must be able to highlight home history as well as have all owners of house on a single page. Word document attached--can also provide files for the house painting, color photos, dorne photo, advertising photo or part of original settler map.
I like this brochure
http://tessavolkind.com/wordpress/quarnby-lodge-museum-brochure/
community stakeholders, residents,
Historic Preservation, House Museums.

```html
<!DOCTYPE html>
<html lang="en">
<head>
<meta charset="utf-8">
<title>Hartwell Homestead Brochure</title>
<link rel="stylesheet" href="https://fonts.googleapis.com/css2?family=Crimson+Pro:ital,wght@0,400;0,600;0,700;1,400&display=swap">
<style>
  :root {
    --brown: #5d3a29;
    --ink: #4a3526;
    --peach: #f6c99a;
    --peach-deep: #e9b27c;
    --paper: #ffffff;
    --ghost: #ececec;
    --ghost-peach: #fbe3c8;
    --cream: #f3ece4;
    --bg: #e8e3dc;
    --rule: #8a7464;
  }
  * { box-sizing: border-box; margin: 0; padding: 0; }
  html, body { width: 1200px; height: 943px; overflow: hidden; background: var(--bg); }
  body { position: relative; font-family: "Crimson Pro", Georgia, serif; color: var(--ink); }

  .spread { position: absolute; left: 250px; width: 700px; height: 452px; overflow: hidden; background: var(--paper); box-shadow: 0 3px 10px rgba(60,40,25,.18); }
  .spread--outer { top: 13px; }
  .spread--inner { top: 478px; }
  .abs { position: absolute; }

  /* outer spread */
  .top-band { left: 0; top: 0; width: 700px; height: 255px; background: var(--brown); }
  .spine-shade { left: 349px; top: 255px; width: 34px; height: 197px; background: linear-gradient(to right, rgba(0,0,0,.08), rgba(0,0,0,0)); }
  .owners { left: 24px; top: 34px; width: 310px; color: #f6eee6; font-size: 6.4px; line-height: 8.4px; }
  .owners__title { font-weight: 700; margin-bottom: 14px; }
  .owners__row { display: flex; margin-bottom: 4.3px; }
  .owners__name { width: 181px; }
  .owners__years { padding-left: 4px; }
  .photo { }
  .photo--house { left: 264px; top: 24px; width: 436px; height: 207px; background: linear-gradient(160deg, #3f5a2c 0%, #b87a2e 35%, #d8b566 55%, #5d6b3a 75%, #6e4a28 100%); }
  .photo--map { left: 22px; top: 283px; width: 107px; height: 100px; background: linear-gradient(135deg, #c9cfcf, #aeb8ba); }
  .photo--ad { left: 144px; top: 285px; width: 174px; height: 100px; background: #efede7; border: 1px solid #d6d2ca; }
  .footer-rule { left: 24px; top: 406px; width: 301px; height: 1px; background: var(--rule); }
  .social { left: 48px; top: 417px; display: flex; align-items: flex-start; gap: 8px; font-size: 6.4px; line-height: 9px; }
  .social__mark { width: 21px; height: 21px; background: var(--ink); flex: none; }
  .social__lead { font-weight: 700; color: #2f2219; }

  /* lockup */
  .lockup__dot { width: 28px; height: 28px; border-radius: 50%; background: var(--brown); }
  .lockup__name { font-size: 20px; line-height: 1; letter-spacing: .6px; text-transform: uppercase; color: var(--brown); white-space: nowrap; }
  .lockup__place, .lockup__year { font-size: 14px; line-height: 1; color: var(--brown); white-space: nowrap; }
  .lockup__ghost { font-size: 77px; line-height: 1; color: var(--ghost); white-space: nowrap; }

  /* inner spread */
  .page-peach { left: 0; top: 0; width: 350px; height: 452px; background: linear-gradient(to right, var(--peach) 70%, var(--peach-deep) 100%); }
  .inner-rule { left: 24px; top: 110px; width: 567px; height: 1px; background: var(--rule); }
  .story { font-size: 6.5px; line-height: 8.45px; color: var(--ink); }
  .story p + p { margin-top: 8.45px; }
  .story__heading { font-size: 8px; line-height: 9.8px; font-weight: 700; color: var(--brown); margin-bottom: 8px; }
  .story--lead { left: 24px; top: 124px; width: 100px; }
  .story--middle { left: 153px; top: 124px; width: 176px; height: 302px; overflow: hidden; }
  .story--right { left: 375px; top: 124px; width: 217px; }
  .story em { font-style: italic; }
  .photo--couple { left: 1px; top: 278px; width: 139px; height: 141px; background: #f4e4dc; padding: 6px 7px 14px; }
  .photo--couple .fill { width: 100%; height: 100%; background: linear-gradient(160deg, #8a8a86, #3e3e3b); }
  .caption { font-size: 5.6px; font-style: italic; color: var(--brown); text-align: center; }
  .photo--couple .caption { margin-top: 2px; }
  .photo--stairs { left: 375px; top: 8px; width: 104px; height: 95px; background: linear-gradient(150deg, #e9e3d8 0%, #b3835a 55%, #7a4e2c 100%); }
  .photo--door { left: 486px; top: 8px; width: 105px; height: 95px; background: linear-gradient(120deg, #2f3a32 0%, #4f8a80 45%, #9cc7bd 100%); }
  .photo--portrait { left: 601px; top: 8px; width: 92px; height: 215px; background: linear-gradient(180deg, #cbb89b, #7c6650); }
  .portrait-caption { left: 601px; top: 223px; width: 92px; height: 55px; background: var(--brown); display: flex; align-items: center; justify-content: center; }
  .portrait-caption .caption { color: #f1d9c0; }
  .photo--painting { left: 359px; top: 287px; width: 334px; height: 158px; background: linear-gradient(180deg, #a9b7c4 0%, #dfe6ea 40%, #2f4f96 62%, #4a6b3c 100%); }
</style>
</head>
<body>

<section class="spread spread--outer">
  <div class="abs top-band"></div>

  <div class="abs owners">
    <p class="owners__title">Owners of 47 Linden Street<br>Peterborough, New Hampshire</p>
    <div class="owners__row"><span class="owners__name">Robert Ashby (grandson of John Ashby) owned the land</span><span class="owners__years">1826</span></div>
    <div class="owners__row"><span class="owners__name">George S. Hartwell and Jane (Lowell) Hartwell</span><span class="owners__years">1826-1828</span></div>
    <div class="owners__row"><span class="owners__name">Deacon Thomas Penrose and Alice (Crane) Penrose (Baptist)</span><span class="owners__years">1828-1839</span></div>
    <div class="owners__row"><span class="owners__name">Elijah Brown Thayer and Achsah (Pell) Thayer<br>(mortgage between Samuel Crane and Thayer is 1845)</span><span class="owners__years">1839-1877</span></div>
    <div class="owners__row"><span class="owners__name">Mary Ellen Thayer</span><span class="owners__years">1877-1898</span></div>
    <div class="owners__row"><span class="owners__name">James Corwin</span><span class="owners__years">1898-1904</span></div>
    <div class="owners__row"><span class="owners__name">Fred Parker Dorne and Grace E. (Marsh) Dorne</span><span class="owners__years">1904-1956</span></div>
    <div class="owners__row"><span class="owners__name">Elinor (Dorne) Ridley and Frank O Ridley<br>(Elinor was born in house on July 29, 1911)</span><span class="owners__years">1955-1998</span></div>
    <div class="owners__row"><span class="owners__name">James H. Vantreese and Maria Ortiz Vantreese<br>(James was nephew of Elinor (Dorne) Ridley)</span><span class="owners__years">1998-2015</span></div>
    <div class="owners__row"><span class="owners__name">Brookholm</span><span class="owners__years">2015-2022</span></div>
    <div class="owners__row"><span class="owners__name">Edward M. Salvo and Albert A. Pruitt, Jr.</span><span class="owners__years">2022</span></div>
  </div>

  <div class="abs photo photo--house" role="img" aria-label="Photograph of the yellow clapboard homestead and barn among autumn trees"></div>

  <div class="abs photo photo--map" role="img" aria-label="Detail of an early settler map showing the river and lot owners"></div>
  <div class="abs photo photo--ad" role="img" aria-label="Newspaper advertisement for H. A. Thayer, wool carder, cloth dresser and wool dyer, Linden Street, 1873"></div>

  <div class="abs footer-rule"></div>
  <div class="abs social">
    <span class="social__mark" aria-hidden="true"></span>
    <p><span class="social__lead">They invite you to join their Neighborly Group</span><br>Hartwell Homestead c. 1826, Dornes Corner, Peterborough, New Hampshire</p>
  </div>

  <div class="abs spine-shade"></div>

  <div class="abs lockup__ghost" style="left:475px; top:332px;">1826</div>
  <div class="abs lockup__dot" style="left:392px; top:300px;"></div>
  <div class="abs lockup__name" style="left:428px; top:317px;">Hartwell Homestead</div>
  <div class="abs lockup__place" style="left:475px; top:343px;">Peterborough, New Hampshire</div>
  <div class="abs lockup__year" style="left:475px; top:357px;">1826</div>
</section>

<section class="spread spread--inner">
  <div class="abs page-peach"></div>

  <div class="abs lockup__ghost" style="left:129px; top:44px; color:var(--ghost-peach);">1826</div>
  <div class="abs lockup__dot" style="left:50px; top:16px;"></div>
  <div class="abs lockup__name" style="left:85px; top:34px;">Hartwell Homestead</div>
  <div class="abs lockup__place" style="left:129px; top:60px;">Peterborough, New Hampshire</div>
  <div class="abs lockup__year" style="left:129px; top:73px;">1826</div>

  <div class="abs inner-rule"></div>

  <div class="abs story story--lead">
    <h2 class="story__heading">The Hartwell Homestead History c. 1826 Peterborough, New Hampshire</h2>
    <p>In 1826, George S. Hartwell and his wife, Jane (Lowell) Hartwell purchased 26 acres from Robert Ashby on the Contoocook River, north of Alden's Woolen Mill in South Peterborough, NH. This parcel was carved out lot #32 which was comprised of 268 acres that were deeded to John Ashby (Robert Ashby's grandfather) by Jeremiah Fisk and John Hale on May 5, 1762. It is believed that</p>
  </div>

  <figure class="abs photo--couple">
    <div class="fill" role="img" aria-label="Black and white photograph of Fred and Grace Dorne seated in their parlor"></div>
    <figcaption class="caption">Fred and Grace Dorne</figcaption>
  </figure>

  <div class="abs story story--middle">
    <p>Hartwell, who was blacksmith, built the house that currently stands at 47 Linden Street in Peterborough, NH. He also built his forge on the site down by the river. It is likely that much of the forged hardware in the home was crafted by him. Feeling the need to leave Peterborough for a new frontier, Hartwell left town with his brother, Asa, to purchase land in the emerging communities of Orleans County, NY. Before doing so, Hartwell sold the home, shop and buildings to Thomas Penrose and his wife Alice (Crane) Penrose in 1828.</p>
    <p>By trade, Thomas Penrose was a cloth dresser and wool-carder. He was also a deeply religious man and served as deacon in the emerging, but still quite small, Baptist community. In those days, small groups of the Baptists and Methodists met in the Bramhall Home for bible study, prayers and singing. The Bramhalls were well known abolitionists and their house served as a stop on the Underground Railroad. Deacon Penrose died in 1839 and his estate was managed by Samuel Crane—very likely a relative of Alice—who protected Alice's dower. The property was then sold to Elijah Brown Thayer and his wife Achsah (Pell) Thayer.</p>
    <p>Elijah was quite industrious and continued to expand the wool mill. He was an early investor in the Ridgeline Railroad and ceded a right of way to the railroad on the homestead. The mill eventually came under the control of his son, Henry A. Thayer, and operated until it burned down on April 20, 1874. Elijah passed away in 1877 and left the home to Mary Ellen Thayer who was most commonly known as "Ellen."</p>
    <p>Ellen Thayer was approached in 1891 by Allie Alden, the owner of the Alden's Mill Complex, to ask if she would be willing to rent out the home to a couple from Boston. This</p>
  </div>

  <div class="abs photo photo--stairs" role="img" aria-label="Photograph of the winding wooden staircase"></div>
  <div class="abs photo photo--door" role="img" aria-label="Photograph of forged door hardware on a weathered teal door"></div>
  <div class="abs photo photo--portrait" role="img" aria-label="Sepia portrait photograph of Marian Galloway standing"></div>
  <div class="abs portrait-caption"><p class="caption">Galloway M</p></div>

  <div class="abs story story--right">
    <p>turned out to be Marian and Edward Galloway, the founders of the Galloway Colony, who ended up spending their first summer in Peterborough, NH in the home. Marian recalls in her writings: <em>"You can't fail to remember the two-story farmhouse almost across from the road from the iron bridge, now occupied by the Dorne Family. It had never been painted and was a lovely soft gray in color. There were really only four rooms and a kitchen, spotlessly clean and adequately furnished, which really didn't mean much but some chairs, tables and beds. Then in the kitchen was something that fascinated me, a stone bowl into which the clearest of water was all the time pouring and then running off into a drain...."</em></p>
    <p>The Dornes lived in this home for the longest time of any owner--and some refer to this area before the bridge, as Dornes Corner. This moment of stewardship began under Fred Parker Dorne and his wife Grace E. (Marsh) Dorne around 1904 and lasted until 2015 when a descendant sold the home. The house is now under the stewardship of Edward M. Salvo and Albert A. Pruitt, Jr. and will be undergoing a significant restoration.</p>
  </div>

  <div class="abs photo photo--painting" role="img" aria-label="Primitive-style painting of the white homestead with blue roofs and attached barn"></div>
</section>

</body>
</html>
```